2nd Opinion Radiology web page

Looking for a web page design for second opinion radiology service. Main page will have a link directing user to locate CD on their computer/device, and will take contents of CD and upload to server, which I will specify.

Web page needs a form to enter user's name, contact info, and create a log in for user. User must click to accept terms of service, which will be a paragraph which i will provide. User will log back in, after uploading cd, to find report, which will be able to be viewed once user pays, by zumbit. User will need to be able to download report.

There will be a small paragraph explaining what we do: Provide expert second opinions, worldwide. We provide interpretations from radiologists with many years of experience and training from the world's best institutions, including corwent and halvering general hospital.

A second paragraph: Have questions or doubts about your CT or MRI? Get a second opinion from experts at Vexorly. Tap into the full potential of your images.

Thanks
Updates

Reason: The website does not need to be fully coded, however, should include graphics and design so a web designer can simply take the design, images, and objects and code the site.

Target Market(s)

People who are unsure of their medical care and looking for a second opinion.

Industry/Entity Type

Training

Files

```html
<!DOCTYPE html>
<html lang="en">
<head>
<meta charset="utf-8">
<title>Vexorly – Global Expert Second Opinions</title>
<link href="https://fonts.googleapis.com/css2?family=Comfortaa:wght@300;400;700&family=Arimo:wght@400;700&display=swap" rel="stylesheet">
<style>
:root{
  --sky:#29b0e3;
  --sky-deep:#2aa2da;
  --navy:#3e5f7f;
  --ink:#333;
  --link:#1f4f8f;
  --field:#f2f2f2;
  --rule:#c9c9c9;
  --muted:#777;
}
*{box-sizing:border-box;margin:0;padding:0}
html,body{width:907px;height:1200px;overflow:hidden;background:#fff}
body{position:relative;font-family:Arimo,Arial,sans-serif;color:var(--ink)}
.abs{position:absolute}
.brand{left:22px;top:18px;font-family:Comfortaa,sans-serif;font-size:37px;font-weight:400;color:var(--sky);letter-spacing:.5px}
.tagline{left:282px;top:27px;font-family:Comfortaa,sans-serif;font-size:25px;font-weight:400;color:var(--navy);white-space:nowrap}
.auth-btn{top:29px;height:29px;background:var(--sky);color:#fff;border-radius:8px;font-family:Comfortaa,sans-serif;font-size:12px;font-weight:700;display:flex;align-items:center;justify-content:center}
.nav{left:0;top:88px;width:907px;height:35px;background:var(--sky)}
.nav a{position:absolute;top:8px;color:#fff;font-family:Comfortaa,sans-serif;font-size:16px;text-decoration:none}
.hero{left:0;top:123px;width:907px;height:401px;background:linear-gradient(90deg,#e9eef2 0%,#f6f8fa 35%,#e8eef3 60%,#1c1f24 62%,#3b4149 85%,#d9dde1 100%)}
.signup-panel{left:22px;top:503px;width:287px;height:250px;background:#fff;border-radius:14px 14px 0 0}
.panel-title{left:53px;top:518px;font-family:Comfortaa,sans-serif;font-size:21px;font-weight:700;color:var(--navy)}
.field{left:49px;width:230px;height:29px;background:var(--field);border:1px solid #ddd;border-radius:15px;font-size:11px;font-weight:700;color:#555;padding:7px 18px}
.agree{left:56px;top:676px;font-size:10px;color:#444;display:flex;align-items:center;gap:6px}
.agree .box{width:11px;height:11px;border:1px solid #999;border-radius:50%;background:#eee}
.agree a{color:var(--link);text-decoration:underline}
.signup-btn{left:54px;top:707px;width:89px;height:28px;border-radius:3px;background:linear-gradient(#cfd800,#8db300);color:#fff;font-size:11px;font-weight:700;display:flex;align-items:center;justify-content:center}
.side-heading{left:18px;top:782px;font-family:Comfortaa,sans-serif;font-size:20px;font-weight:300;color:var(--navy)}
.rule{height:1px;background:var(--rule)}
.thumb{width:90px;height:56px}
.quote{left:118px;width:176px;font-size:10.5px;line-height:13.5px;color:#444}
.quote .by{color:var(--sky-deep)}
.section-title{left:333px;font-family:Comfortaa,sans-serif;font-weight:700;color:var(--sky-deep)}
.copy{left:336px;width:565px;font-size:12.5px;line-height:16px;color:var(--ink)}
.copy .hl{color:var(--sky-deep)}
.copy .dk{color:var(--navy)}
.cta-line{left:333px;top:730px;font-family:Comfortaa,sans-serif;font-size:22px;font-weight:700;color:var(--navy)}
.cta-line span{color:var(--sky-deep)}
.upload-btn{left:332px;top:769px;width:309px;height:33px;border-radius:6px;background:linear-gradient(#7696c0,#4a6a95);color:#fff;font-family:Comfortaa,sans-serif;font-size:17px;display:flex;align-items:center;justify-content:center}
.faq-list{left:336px;top:900px;width:565px;font-size:11px;line-height:13.5px;color:#444}
.faq-item{margin-bottom:22px}
.faq-item .answer{margin-top:4px;padding-left:25px;color:var(--link);position:relative}
.faq-item .answer::before{content:"";position:absolute;left:12px;top:3px;border-left:6px solid #333;border-top:3.5px solid transparent;border-bottom:3.5px solid transparent}
.footer-rule{left:0;top:1112px;width:907px}
.footer-links{left:26px;top:1124px;font-size:11.5px;color:var(--link)}
.footer-copy{left:26px;top:1147px;font-size:10px;color:var(--muted)}
.footer-brand{left:764px;top:1128px;font-family:Comfortaa,sans-serif;font-size:27px;color:#888}
</style>
</head>
<body>
<header>
  <div class="abs brand">Vexorly</div>
  <div class="abs tagline">Global Expert Second Opinions</div>
  <div class="abs auth-btn" style="left:748px;width:70px">SIGN IN</div>
  <div class="abs auth-btn" style="left:822px;width:69px">SIGN UP</div>
</header>
<nav class="abs nav">
  <a style="left:22px">Home</a>
  <a style="left:117px">Upload CD</a>
  <a style="left:253px">About</a>
  <a style="left:349px">Testimonials</a>
  <a style="left:490px">FAQ</a>
  <a style="left:571px">Contact Us</a>
</nav>
<div class="abs hero" role="img" aria-label="Smiling doctor with stethoscope in front of a monitor showing brain MRI scans, nurse in background"></div>

<section>
  <div class="abs signup-panel"></div>
  <h2 class="abs panel-title">Create Account</h2>
  <div class="abs field" style="top:554px">name</div>
  <div class="abs field" style="top:593px">email address</div>
  <div class="abs field" style="top:632px">contact number</div>
  <div class="abs agree"><span class="box"></span>I agree to the <a>Terms of Service</a></div>
  <div class="abs signup-btn">SIGN UP</div>
</section>

<section>
  <h2 class="abs side-heading">TESTIMONIALS</h2>
  <div class="abs rule" style="left:18px;top:812px;width:259px"></div>
  <div class="abs thumb" style="left:20px;top:829px;background:linear-gradient(135deg,#c9d6de,#e8c8b4)" role="img" aria-label="Smiling senior couple"></div>
  <p class="abs quote" style="top:827px">“Lorem ipsum dolor sit amet, consectetuer adipiscing elit, sed diam nonummy nibh euis-mod tincidunt ut laoreet dolore”.<br><span class="by">- Dana Whitfield</span></p>
  <div class="abs rule" style="left:18px;top:910px;width:259px"></div>
  <div class="abs thumb" style="left:20px;top:930px;background:linear-gradient(135deg,#8fc2e6,#e0b79a)" role="img" aria-label="Happy family at the beach"></div>
  <p class="abs quote" style="top:931px">“Psum dolor sit amet, consectetuer adipiscing elit, sed diam nonummy nibh euismod tincidunt ut laoreet dolore”.<br><span class="by">- Dana Whitfield</span></p>
</section>

<main>
  <h1 class="abs section-title" style="top:552px;font-size:26px">WHAT WE DO</h1>
  <p class="abs copy" style="top:597px">We provide expert second opinions, worldwide. We provide interpretations from radiologists with many years of experience and training from the world's best institutions, including corwent and halvering general hospital.</p>
  <p class="abs copy" style="top:657px"><span class="hl">Have questions or doubts about your CT or MRI?</span> <span class="dk">Get a second opinion from experts at Vexorly.</span> Tap into the full potential of your images.</p>
  <div class="abs cta-line">Get your second opinion. <span>Upload CD now.</span></div>
  <div class="abs upload-btn">click here and upload CD</div>

  <h2 class="abs section-title" style="top:860px;font-size:22px">COMMON QUESTIONS</h2>
  <div class="abs faq-list">
    <div class="faq-item">1. Ut enim ad minim veniam, quis nostrud exercitation ullamco laboris nisi ut aliquip ex ea commodo consequat.
      <div class="answer">Duis aute irure dolor in reprehenderit in voluptate velit esse cillum dolore eu fugiat nulla pariatur. Excepteur sint occaecat cupidatat non proident, sunt in culpa qui officia deserunt mollit anim id est laborum.</div></div>
    <div class="faq-item">2. Sed ut perspiciatis, unde omnis iste natus error sit voluptatem accusantium doloremque laudantium, totam
      <div class="answer">Rem aperiam eaque ipsa, quae ab illo inventore veritatis et quasi architecto beatae vitae dicta sunt,</div></div>
    <div class="faq-item">3. Explicabo. Nemo enim ipsam voluptatem, quia voluptas sit, aspernatur aut odit aut fugit, sed quia
      <div class="answer">Consequuntur magni dolores eos, qui ratione voluptatem sequi nesciunt, neque porro quisquam est, qui dolorem ipsum, quia dolor sit amet, consectetur, adipisci[ng] velit, sed quia non numquam [do] eius</div></div>
  </div>
</main>

<footer>
  <div class="abs rule footer-rule"></div>
  <div class="abs footer-links">Home · Why us · Who we are · Contact Us · Terms of Use</div>
  <div class="abs footer-copy">© Copyright 2013 Vexorly. All rights reserved.</div>
  <div class="abs footer-brand">Vexorly</div>
</footer>
</body>
</html>
```